Biz card & Stationary
Hollin Ridge Materials
Modern
Dana Wexler
Sales Manager
48217 Quimby Lane
P. O. Box 5179
Marlow Falls, NC 24619
dwexler@lumarbo.com
www.lumarbo.com

```html
<!DOCTYPE html>
<html lang="en">
<head>
<meta charset="utf-8">
<title>Hollin Ridge Materials – Business Cards</title>
<link href="https://fonts.googleapis.com/css2?family=Arimo:wght@400;700&display=swap" rel="stylesheet">
<style>
  :root {
    --stage: #e9e9e6;
    --card-edge: #d6d8dc;
    --brand-blue: #1d5fa8;
    --brand-navy: #0d2f66;
    --deep-blue: #123f7e;
    --mid-blue: #2a6bbd;
    --text-grey: #555a60;
    --faint-grey: #e4e6ea;
    --faint-grey-inner: #dcdfe4;
    --web-blue: #2a6bbd;
    --white: #ffffff;
  }
  * { margin: 0; padding: 0; box-sizing: border-box; }
  html, body { width: 1200px; height: 911px; overflow: hidden; }
  body {
    background: var(--stage);
    font-family: "Arimo", Arial, sans-serif;
    position: relative;
  }
  .card {
    position: absolute;
    width: 420px;
    height: 234px;
    border-radius: 12px;
    overflow: hidden;
  }
  .card--front {
    left: 143px; top: 304px;
    background: linear-gradient(180deg, #ffffff 0%, #f2f3f5 100%);
    border: 1px solid var(--card-edge);
    z-index: 2;
  }
  .card--back {
    left: 630px; top: 212px;
    background: radial-gradient(circle at 58% 42%, var(--mid-blue) 0%, var(--deep-blue) 55%, var(--brand-navy) 100%);
  }
  .card--reverse {
    left: 363px; top: 516px;
    background: linear-gradient(180deg, #ffffff 0%, #f1f2f4 100%);
    border: 1px solid var(--card-edge);
    z-index: 3;
  }

  .brand {
    position: absolute;
    right: 20px; top: 22px;
    width: 210px;
    text-align: center;
  }
  .brand__dot {
    display: block;
    width: 44px; height: 44px;
    margin: 0 auto 6px;
    border-radius: 50%;
    background: var(--brand-blue);
  }
  .brand__name {
    font-weight: 700;
    font-size: 19px;
    line-height: 1.05;
    color: var(--brand-blue);
    text-transform: uppercase;
  }
  .brand__tagline {
    margin-top: 4px;
    font-size: 6.5px;
    color: var(--text-grey);
    text-transform: uppercase;
    letter-spacing: 0.2px;
  }

  .contact {
    position: absolute;
    left: 24px; top: 112px;
    color: var(--text-grey);
  }
  .contact__name {
    font-size: 15px;
    font-weight: 700;
    color: var(--brand-blue);
  }
  .contact__title { font-size: 8.5px; margin-top: 2px; }
  .contact__lines { margin-top: 22px; font-size: 8.5px; line-height: 1.55; }
  .web {
    position: absolute;
    font-size: 8px;
    color: var(--web-blue);
  }
  .card--front .web { left: 24px; bottom: 20px; }

  .faint-ring { position: absolute; }
  .card--back .faint-ring { left: 40px; top: 2px; }
  .card--reverse .faint-ring { left: -4px; top: -10px; }

  .mini-mark {
    position: absolute;
    right: 18px; bottom: 14px;
    text-align: center;
  }
  .mini-mark__dot {
    display: block;
    width: 26px; height: 26px;
    margin: 0 auto 4px;
    border-radius: 50%;
  }
  .mini-mark__name { font-size: 6.5px; font-weight: 700; text-transform: uppercase; }
  .mini-mark .web { position: static; display: block; margin-top: 2px; font-size: 6.5px; }

  .card--back .mini-mark__dot { background: var(--white); }
  .card--back .mini-mark__name, .card--back .mini-mark .web { color: var(--white); }
  .card--reverse .mini-mark__dot { background: var(--brand-blue); }
  .card--reverse .mini-mark__name { color: var(--brand-blue); }
</style>
</head>
<body>

  <section class="card card--back" aria-label="Card back">
    <svg class="faint-ring" width="200" height="200" viewBox="0 0 200 200" aria-hidden="true">
      <circle cx="100" cy="100" r="95" fill="#ffffff" fill-opacity="0.08"/>
      <circle cx="100" cy="100" r="70" fill="#ffffff" fill-opacity="0.06"/>
    </svg>
    <div class="mini-mark">
      <span class="mini-mark__dot"></span>
      <div class="mini-mark__name">Hollin Ridge Materials</div>
      <span class="web">www.lumarbo.com</span>
    </div>
  </section>

  <section class="card card--front" aria-label="Card front">
    <div class="brand">
      <span class="brand__dot"></span>
      <div class="brand__name">Hollin Ridge Materials</div>
      <div class="brand__tagline">A division of Tarnwell Surface Group, LLC</div>
    </div>
    <div class="contact">
      <div class="contact__name">Dana Wexler</div>
      <div class="contact__title">Sales Manager</div>
      <div class="contact__lines">
        48217 Quimby Lane, P. O. Box 5179, Marlow Falls, NC 24619<br>
        T: 919-555-0142 &nbsp;|&nbsp; E: dwexler@lumarbo.com
      </div>
    </div>
    <span class="web">www.lumarbo.com</span>
  </section>

  <section class="card card--reverse" aria-label="Card reverse, white">
    <svg class="faint-ring" width="230" height="230" viewBox="0 0 230 230" aria-hidden="true">
      <circle cx="115" cy="115" r="108" fill="var(--faint-grey)"/>
      <circle cx="115" cy="115" r="82" fill="var(--faint-grey-inner)"/>
    </svg>
    <div class="mini-mark">
      <span class="mini-mark__dot"></span>
      <div class="mini-mark__name">Hollin Ridge Materials</div>
      <span class="web">www.lumarbo.com</span>
    </div>
  </section>

</body>
</html>
```